Veranta - Solution provider in business consulting

Veranta is a swiss based company providing solutions for developing markets. The business covers various fields of business consulting, such as supply chain, product costs, quality management and manufacturing management. The Business operates in a efficient, straight and solution oriented manner.
The final design should communicate these characteristics. Asian people as well as as western people shall identify the qualities of the company at first sight.
The customer needs business cards with a simple view but an recognizable design, printed in high quality. Engraved elements such as the globe or simple words are possible.
Available colors are: (RAL)
102/102/102
51/102/102
153/204/153
255/102/51
Font: Calibri
Industry/Entity Type
Business
Look and feel
Each slider illustrates characteristics of the customer's brand and the style your logo design should communicate.

```html
<!DOCTYPE html>
<html lang="en">
<head>
<meta charset="utf-8">
<title>Veranta – Business Card</title>
<link href="https://fonts.googleapis.com/css2?family=Carlito:wght@400;700&display=swap" rel="stylesheet">
<style>
  :root {
    --stage: #e6e4e0;
    --paper: #ffffff;
    --paper-shade: #eeeeee;
    --ink: #666666;
    --ink-dark: #4a4a4a;
    --ink-soft: #8a8a8a;
    --back-light: #6e6e6e;
    --back-dark: #3c3c3c;
    --back-mark: #e4e4e4;
  }
  * { box-sizing: border-box; margin: 0; padding: 0; }
  html, body {
    width: 1200px; height: 950px; overflow: hidden;
    background: var(--stage);
    font-family: "Carlito", "Calibri", sans-serif;
  }
  .stage {
    width: 1200px; height: 950px;
    display: flex; flex-direction: column; align-items: center; justify-content: center;
    gap: 50px;
  }
  .card {
    position: relative;
    width: 700px; height: 400px;
    border-radius: 4px;
    box-shadow: 0 10px 28px rgba(0,0,0,.18);
    overflow: hidden;
  }
  /* front */
  .card--front {
    background: linear-gradient(160deg, var(--paper) 40%, var(--paper-shade) 100%);
    color: var(--ink);
  }
  .brand {
    position: absolute; top: 92px; right: 60px;
    display: flex; align-items: center; gap: 12px;
  }
  .brand__dot {
    width: 40px; height: 40px; border-radius: 50%;
    background: var(--ink);
  }
  .brand__name {
    font-size: 56px; font-weight: 400; color: var(--ink);
    letter-spacing: 1px; line-height: 1;
  }
  .person {
    position: absolute; left: 56px; top: 148px;
  }
  .person__name { font-size: 24px; font-weight: 700; color: var(--ink-dark); }
  .person__role { font-size: 17px; color: var(--ink-soft); margin-top: 2px; }
  .contact {
    list-style: none;
    position: absolute; left: 56px; top: 222px;
    font-size: 19px; line-height: 25px; color: var(--ink-dark);
  }
  .contact li { display: flex; align-items: center; gap: 9px; }
  .contact svg { width: 16px; height: 16px; fill: var(--ink); flex: none; }
  .divider {
    position: absolute; left: 318px; top: 282px;
    width: 1px; height: 64px; background: var(--ink-soft);
  }
  .company {
    position: absolute; left: 338px; top: 282px;
    font-size: 19px; line-height: 23px; color: var(--ink);
  }
  .company__name { font-weight: 700; color: var(--ink-dark); }

  /* back */
  .card--back {
    background: linear-gradient(135deg, var(--back-light) 0%, var(--back-dark) 100%);
  }
  .back-mark {
    position: absolute; left: 50%; top: 50%;
    transform: translate(-50%, -58%);
    width: 150px; height: 150px; border-radius: 50%;
    background: var(--back-mark);
  }
  .back-url {
    position: absolute; left: 50%; top: 262px;
    transform: translateX(-50%);
    font-size: 24px; color: var(--back-mark); letter-spacing: 1px;
  }
</style>
</head>
<body>
<main class="stage">
  <section class="card card--front" aria-label="Business card front">
    <div class="brand">
      <span class="brand__dot"></span>
      <span class="brand__name">veranta</span>
    </div>

    <div class="person">
      <p class="person__name">Marco Keller</p>
      <p class="person__role">CEO</p>
    </div>

    <ul class="contact">
      <li>
        <svg viewBox="0 0 16 16" aria-hidden="true"><path d="M2 5c0-2 2-3 6-3s6 1 6 3v1h-3V4.5H5V6H2zM4 7h8l2 6H2z"/></svg>
        +41 71 555 0182
      </li>
      <li>
        <svg viewBox="0 0 16 16" aria-hidden="true"><path d="M4 1h8v14H4zM5.5 2.5v9h5v-9z"/></svg>
        +41 79 555 0347
      </li>
      <li>
        <svg viewBox="0 0 16 16" aria-hidden="true"><path d="M1 3h14v10H1zM2.5 4.5 8 9l5.5-4.5z"/></svg>
        marco.keller@veranta.ch
      </li>
      <li>
        <svg viewBox="0 0 16 16" aria-hidden="true"><circle cx="8" cy="8" r="7"/></svg>
        www.veranta.ch
      </li>
    </ul>

    <span class="divider"></span>
    <div class="company">
      <p class="company__name">Veranta GmbH</p>
      <p>Feldweg 14, 9000 Musterdorf</p>
      <p>Switzerland</p>
    </div>
  </section>

  <section class="card card--back" aria-label="Business card back">
    <span class="back-mark"></span>
    <p class="back-url">veranta.ch</p>
  </section>
</main>
</body>
</html>
```